Weihnachtskarte für überregionalen Mandantenkreis einer Unternehmensberatung
Zielgruppe
Die KOLVEN Steuerberatungsgesellschaft mbH ist überregional tätig und berät Kunden in steuerlichen und betriebswirtschaftlichen Belangen. Ein Tätigkeitsschwerpunkt unseres Unternehmens ist die steuerliche und betriebswirtschaftliche BEgleitung von Insolvenzverfahren im Auftrag renomierter Insolvenzverwalterkanzleien in Deutschland.
Aufgabenstellung
Die Weihnachtskarte sollte in einem puren, schlichten Look gehalten sein. Der Kreativität sind dabei keine Grenzen gesetzt. Wir können uns sowohl eher statische Muster/Grafiken als auch weihnachtliche Illustrationen vorstellen. Diese dürfen dann auch verspielt wirken, wobei dabei auch mit Kontrasten zu unserem klaren Corporate-Design gearbeitet werden sollte. Unsere Standardfarben in Firmenprsäentationen sind die folgenden Codes:
r149/g179/b215
r165/g164/b167
r195/g214/b155
und diverse Grautöne
Die Karte sollte folgende Inhalte besitzen:
1. Firmenschriftzug/Logo
Gesellschaftsname: KOLVEN Steuerberatungsgesellschaft mbH
2. Die Standorte unserer Gesellschaft
3. Kurzer Weihnachtsgruß, der so positioniert sein sollte, dass in dessen Umfeld Platz für einen handschriftlichen Gruß und eine Unterschrift bleibt
4. unsere Internetseite ("www.kolven-beispiel.de")
Als Anlage ist ein Datenblatt für die Erstellung der geeigneten Druckdatei beigefügt. Geplant ist die Karte im Format DIN lang (21x9,8), wobei die Nut an der Längsseite verlaufen soll. Der Karte wird dabei im Querformat bedruckt.

```html
<!DOCTYPE html>
<html lang="de">
<head>
<meta charset="utf-8">
<title>KOLVEN Weihnachtskarte</title>
<link href="https://fonts.googleapis.com/css2?family=Pinyon+Script&family=Questrial&family=Open+Sans:wght@400;700&display=swap" rel="stylesheet">
<style>
  :root{
    --bg:#e7e7e9;
    --navy-dark:#0e3874;
    --navy:#1b4d8c;
    --blue-light:#2f6d9f;
    --band:#ffffff;
    --script-blue:#174f93;
    --text-grey:#4a4a4c;
    --inner-grey:#c9c9cb;
    --inner-green:#c3d69b;
    --paper:#ffffff;
  }
  *{box-sizing:border-box;margin:0;padding:0}
  html,body{width:1200px;height:943px;overflow:hidden;background:var(--bg)}
  .spread{position:absolute;top:207px;width:560px;height:528px;overflow:hidden;box-shadow:0 2px 8px rgba(0,0,0,.18)}
  .spread--outside{left:25px}
  .spread--inside{left:615px;background:var(--paper)}

  /* outside */
  .back-panel{position:absolute;left:0;top:0;width:100%;height:264px;
    background:linear-gradient(180deg,var(--navy-dark) 0%,#164683 70%,var(--navy) 100%)}
  .front-panel{position:absolute;left:0;top:264px;width:100%;height:264px;
    background:linear-gradient(180deg,var(--navy) 0%,#21568f 100%)}
  .fold-line{position:absolute;left:0;top:264px;width:100%;height:1px;background:rgba(255,255,255,.35)}
  .imprint{position:absolute;left:20px;top:12px;width:520px;height:52px;transform:rotate(180deg);
    font-family:"Open Sans",sans-serif;color:#fff;font-size:5.6px;line-height:1.7}
  .imprint__name{font-weight:700;font-size:6.6px;margin-bottom:5px}
  .imprint__row{display:flex;justify-content:space-between;align-items:flex-end}
  .imprint__col{white-space:nowrap}
  .imprint__url{font-weight:700;font-size:6px}

  .flake{position:absolute;border-radius:50%;
    background:radial-gradient(circle,rgba(255,255,255,.55) 0%,rgba(255,255,255,.2) 55%,rgba(255,255,255,0) 72%)}
  .flake--blue{background:radial-gradient(circle,rgba(23,79,147,.55) 0%,rgba(23,79,147,.2) 55%,rgba(23,79,147,0) 72%)}
  .flake--grey{background:radial-gradient(circle,rgba(180,180,184,.5) 0%,rgba(180,180,184,.18) 55%,rgba(180,180,184,0) 72%)}
  .flake--mixed{background:radial-gradient(circle,rgba(195,214,155,.75) 0%,rgba(201,201,203,.45) 50%,rgba(255,255,255,0) 72%)}

  .wordmark{position:absolute;font-family:"Questrial",sans-serif;letter-spacing:2px;font-size:15px;display:flex;align-items:center;gap:6px}
  .wordmark__mark{width:9px;height:9px}
  .wordmark--front{right:40px;top:17px;color:#fff}
  .wordmark--front .wordmark__mark{background:#fff}
  .wordmark--inside{left:18px;top:18px;color:var(--navy)}
  .wordmark--inside .wordmark__mark{background:var(--navy)}

  .greeting-band{position:absolute;left:0;top:118px;width:100%;height:79px;background:var(--band)}
  .greeting-edge{position:absolute;left:0;top:197px;width:100%;height:12px;
    background:linear-gradient(180deg,#ffffff 0%,#cfdcea 100%)}
  .lower-band{position:absolute;left:0;top:209px;width:100%;height:55px;background:var(--blue-light)}
  .greeting{position:absolute;left:135px;top:127px;color:var(--script-blue)}
  .greeting__main{font-family:"Pinyon Script",cursive;font-size:40px;line-height:1;font-weight:400}
  .greeting__sub{font-family:"Questrial",sans-serif;font-size:16px;margin:-4px 0 0 104px;line-height:1}

  /* inside */
  .inside-fold{position:absolute;left:0;top:262px;width:100%;height:6px;
    background:linear-gradient(180deg,rgba(0,0,0,0) 0%,rgba(0,0,0,.06) 50%,rgba(0,0,0,0) 100%)}
  .inside-shade{position:absolute;left:0;top:0;width:100%;height:528px;
    background:linear-gradient(160deg,rgba(255,255,255,0) 55%,rgba(0,0,0,.04) 100%)}
  .message{position:absolute;left:0;top:306px;width:100%;text-align:center;
    font-family:"Pinyon Script",cursive;font-size:14.5px;line-height:17px;color:var(--text-grey)}
</style>
</head>
<body>
  <section class="spread spread--outside" aria-label="Außenseite der Karte">
    <div class="back-panel">
      <div class="imprint">
        <p class="imprint__name">KOLVEN Steuerberatungsgesellschaft mbH</p>
        <div class="imprint__row">
          <div class="imprint__col">Am Kaiufer 14 | 20457 Hamburg | T +49 40 5550182<br>Lindenhof 7 | 04109 Leipzig | T +49 341 5550419</div>
          <div class="imprint__col">Birkenweg 22 | 80331 München | T +49 89 5550736<br>Münsterplatz 9 | 89073 Ulm | T +49 731 5550268</div>
          <div class="imprint__col imprint__url">www.kolven-beispiel.de</div>
        </div>
      </div>
      <span class="flake" role="img" aria-label="Schneeflocke" style="left:96px;top:112px;width:40px;height:40px"></span>
      <span class="flake" role="img" aria-label="Schneeflocke" style="left:32px;top:140px;width:70px;height:70px"></span>
      <span class="flake" role="img" aria-label="Schneeflocke" style="left:317px;top:154px;width:50px;height:50px"></span>
      <span class="flake" role="img" aria-label="Schneeflocke" style="left:446px;top:194px;width:50px;height:50px"></span>
      <span class="flake" role="img" aria-label="Schneeflocke" style="left:134px;top:226px;width:68px;height:68px"></span>
    </div>
    <div class="fold-line"></div>
    <div class="front-panel">
      <div class="wordmark wordmark--front"><span class="wordmark__name">KOLVEN</span><span class="wordmark__mark"></span></div>
      <span class="flake" role="img" aria-label="Schneeflocke" style="left:31px;top:20px;width:104px;height:104px"></span>
      <span class="flake" role="img" aria-label="Schneeflocke" style="left:350px;top:70px;width:60px;height:60px"></span>
      <div class="greeting-band"></div>
      <div class="greeting-edge" role="img" aria-label="Gezackte Kante aus weißen Dreiecken"></div>
      <div class="lower-band"></div>
      <span class="flake flake--blue" role="img" aria-label="Blaue Schneeflocke" style="left:478px;top:116px;width:48px;height:48px"></span>
      <div class="greeting">
        <p class="greeting__main">Merry Christmas</p>
        <p class="greeting__sub">and Happy New Year!</p>
      </div>
    </div>
  </section>

  <section class="spread spread--inside" aria-label="Innenseite der Karte">
    <div class="inside-shade"></div>
    <div class="wordmark wordmark--inside"><span class="wordmark__name">KOLVEN</span><span class="wordmark__mark"></span></div>
    <span class="flake flake--mixed" role="img" aria-label="Schneeflocke in Grün und Grau" style="left:208px;top:55px;width:140px;height:140px"></span>
    <span class="flake flake--grey" role="img" aria-label="Graue Schneeflocke" style="left:500px;top:15px;width:70px;height:70px"></span>
    <span class="flake flake--grey" role="img" aria-label="Graue Schneeflocke" style="left:22px;top:223px;width:54px;height:54px"></span>
    <span class="flake flake--grey" role="img" aria-label="Graue Schneeflocke" style="left:-30px;top:258px;width:84px;height:84px"></span>
    <div class="inside-fold"></div>
    <p class="message">Für das entgegengebrachte Vertrauen<br>und die angenehme Zusammenarbeit bedanken wir uns<br>und wünschen Ihnen eine gesegnete Weihnachtszeit,<br>Gesundheit und ein erfolgreiches neues Jahr.</p>
  </section>
</body>
</html>
```